'The Lindqvist Draft' needs a movie poster

We need a movie poster for our short film coming up.

Genre: Drama/Mystery

Plot/Synopsis:
The Lindqvist Draft explores the fraught relationship between creation and destiny, the creator and the created: inspiration, obsession, destruction.
In the opening scene we are introduced to Walter Lindqvist and a young writer, Nora, whose stories play out decades apart and yet are intricately linked. Walter struggles with a block during the writing of his first novel; Nora, obsessed with uncovering her own past is inexplicably drawn to Lindqvist’s house and accepts a room for let from Greta, a strange woman who also resides there. As the two woman avoid delving too deep into each other’s pasts, suspicious of their intentions, Nora discovers that Walter mysteriously died without finishing his debut novel and Greta is most certainly holding something back.
Tensions are raised as Nora settles into Walter’s office and investigates the chattels left behind on his bureau. Accidentally marking a waiting page of manuscript, she unlocks a sixth sense of déjà vu, obsession seeps into possession and the voice of the author comes to life in an unexpected manner in order to enact his long awaited epilogue. With-in the novel, Nora finds the key to her past and confronts Greta with what she uncovers.
Dealing with the dark and destructive side of creativity, The Lindqvist Draft is an edgy mystery with a lurking subtext; Or is it just the greatest plot twist penned by a non-living author.

I have attached for you some images taken from the video camera.
Feel free to add any graphic if you want. I don't have a particular idea of how I want the poster so far so you are pretty free as long as The poster is appealing to the public and make them want to see the film and is related to the synopsis.

-An MoVantReel Production see our logo attached in the pictures
-Director by Tomaso Ruffini
-screenplay by Danny Wolcott

-Staring: (by order of importance)
Marthe Quillon
Lorna Brisbee
Glen Mabbott
Rolf Dunning

-Log line: Are you here to fill those pages?

Feel free to use any of those pictures or any of your design if you have ideas. Or even combine some of our pics with some design of yours.
Nora the lead actress is the young girl on the picture. she has to be in the poster. The other older woman is Greta! She is the supporting role-an important key of the story but very mysterious. (she doesn’t have to be in the poster)

Also it is IMPORTANT for me to have this poster in a format that I can edit as I will need to add some more names in the crew & music credit. Important that you could make the changes for me too include in this price.

Target Market(s)

Film festivals

Industry/Entity Type

Movie

Colors

Designer to choose colors to be used in the design.

Requirements
Must have
• The lead Nora (the young girl) in the poster.
• The producer logo must appear.
• A good title writing style.
• Drama feel.
Nice to have
• It would be nice to incorporate a gun in the design of the title 'The Lindqvist Draft'

```html
<!DOCTYPE html>
<html lang="en">
<head>
<meta charset="utf-8">
<title>The Lindqvist Draft — Poster</title>
<link rel="stylesheet" href="https://fonts.googleapis.com/css2?family=Inter:wght@700;800;900&display=swap">
<style>
  :root {
    --paper: #ffffff;
    --cream: #e9dcc0;
    --red: #dc0a05;
    --ink: #0b0b0b;
    --photo-light: #bdbdbd;
    --photo-dark: #3a3a3a;
  }
  html, body {
    margin: 0;
    padding: 0;
    width: 881px;
    height: 1200px;
    overflow: hidden;
    background: var(--paper);
  }
  .poster {
    display: block;
    width: 881px;
    height: 1200px;
  }
  .title {
    font-family: "Inter", Arial, sans-serif;
    font-weight: 900;
  }
  .director {
    font-family: "Inter", Arial, sans-serif;
    font-weight: 800;
    font-size: 17px;
    fill: var(--cream);
  }
  .credits {
    font-family: "Inter", Arial, sans-serif;
    font-weight: 800;
    font-size: 18.5px;
    fill: var(--ink);
  }
  .studio-name {
    font-family: "Inter", Arial, sans-serif;
    font-weight: 700;
    font-size: 13px;
    fill: var(--ink);
  }
</style>
</head>
<body>
<svg class="poster" viewBox="0 0 881 1200" xmlns="http://www.w3.org/2000/svg">
  <defs>
    <linearGradient id="portrait-tone" x1="0" y1="0" x2="1" y2="0">
      <stop offset="0" stop-color="var(--photo-light)"/>
      <stop offset="0.55" stop-color="#8c8c8c"/>
      <stop offset="1" stop-color="var(--photo-dark)"/>
    </linearGradient>
    <clipPath id="title-letters">
      <text class="title" x="102" y="676" font-size="440" textLength="676" lengthAdjust="spacingAndGlyphs">THE</text>
      <text class="title" x="96" y="778" font-size="116" textLength="670" lengthAdjust="spacingAndGlyphs">LINDQVIST</text>
    </clipPath>
  </defs>

  <!-- cream sheet -->
  <rect class="sheet" x="74" y="56" width="728" height="1083" fill="var(--cream)"/>

  <!-- red slanted block -->
  <polygon class="red-block" points="134,72 757,123 740,1003 120,957" fill="var(--red)"/>

  <text class="director" x="138" y="147">A FILM BY TOMASO RUFFINI</text>

  <!-- title -->
  <text class="title" x="102" y="676" font-size="440" fill="var(--ink)" textLength="676" lengthAdjust="spacingAndGlyphs">THE</text>
  <text class="title" x="96" y="778" font-size="116" fill="var(--ink)" textLength="670" lengthAdjust="spacingAndGlyphs">LINDQVIST</text>

  <!-- portrait of Nora shown through the title letters -->
  <g clip-path="url(#title-letters)">
    <rect class="portrait" x="480" y="357" width="298" height="421" fill="url(#portrait-tone)"
          role="img" aria-label="Black and white profile portrait of Nora, the lead, seen through the title letters"/>
  </g>

  <text class="title" x="120" y="976" font-size="256" fill="var(--cream)" textLength="628" lengthAdjust="spacingAndGlyphs">DRAFT</text>

  <!-- credits -->
  <text class="credits" x="104" y="1040">The LINDQVIST DRAFT screenplay by DANNY WOLCOTT,</text>
  <text class="credits" x="104" y="1068">starring Marthe QUILLON - Lorna BRISBEE - Glen MABBOTT</text>
  <text class="credits" x="104" y="1096">- Rolf DUNNING</text>

  <!-- studio mark -->
  <rect class="studio-square" x="716" y="1040" width="18" height="18" fill="var(--red)"/>
  <text class="studio-name" x="690" y="1088">MoVantReel</text>
</svg>
</body>
</html>
```